WordPress Website for Pain Relief Clinic

I need a WordPress website designed for my laser pain relief clinic. It needs to be a professional, responsive design with 7 pages: Home, Why Choose Us, Treatable Conditions, Testimonials, FAQ, Franchising, Contact Us. Here is logo: https://files.brivoltcdn.com/media.t-w-e-n.com/sitebuilder/472/CalvexaLogoHighQuality.png

Target Market(s)

people with pain,elderly adults,injuries,soreness

Industry/Entity Type

Clinic

Number of Pages Required

5+ page

Colors
0792cd
85abd2

```html
<!DOCTYPE html>
<html lang="en">
<head>
<meta charset="utf-8">
<title>Calvexa Laser Pain Relief</title>
<link rel="stylesheet" href="https://fonts.googleapis.com/css2?family=Oswald:wght@400;500&family=Open+Sans:wght@400;600;700&display=swap">
<style>
:root{
  --blue:#0792cd;
  --blue-soft:#85abd2;
  --blue-deep:#1f6fae;
  --nav:#3e8fd1;
  --nav-active:#6fb0e4;
  --ink:#333;
  --muted:#666;
  --footer:#0b0b0b;
  --footer-bar:#2a2a2a;
  --white:#fff;
}
*{margin:0;padding:0;box-sizing:border-box}
html,body{width:867px;height:1200px;overflow:hidden}
body{position:relative;background:var(--white);font-family:"Open Sans",Arial,sans-serif;color:var(--ink)}
.site-header{position:absolute;left:0;top:0;width:867px;height:81px;background:linear-gradient(180deg,#eef5fb,#dfeaf5)}
.brand{position:absolute;left:22px;top:24px;font-family:"Oswald",Arial,sans-serif;font-weight:500;font-size:27px;color:var(--blue-deep);letter-spacing:.5px}
.phone-pill{position:absolute;right:52px;top:24px;height:26px;padding:0 14px 0 6px;border-radius:13px;background:var(--nav);color:var(--white);font-size:11px;font-weight:600;display:flex;align-items:center;gap:6px}
.phone-pill .ico{width:17px;height:17px;border-radius:50%;background:var(--white);display:flex;align-items:center;justify-content:center}
.main-nav{position:absolute;left:80px;top:64px;width:707px;height:28px;background:var(--nav);display:flex;align-items:stretch;padding-left:14px}
.main-nav a{color:var(--white);text-decoration:none;font-size:9.5px;font-weight:700;display:flex;align-items:center;padding:0 13px}
.main-nav a.active{background:var(--nav-active)}
.hero{position:absolute;left:0;top:81px;width:867px;height:330px;background:linear-gradient(90deg,#9cc4e6 0%,#c9dff0 45%,#e7eff6 100%);overflow:hidden}
.hero-photo{position:absolute;right:0;top:0;width:520px;height:330px;background:radial-gradient(ellipse at 60% 50%,#f1e4dc 0%,#d9d6de 40%,rgba(201,223,240,0) 75%)}
.hero-band{position:absolute;left:0;top:170px;width:867px;height:100px;background:linear-gradient(90deg,rgba(31,111,174,.55),rgba(31,111,174,.05) 70%)}
.hero-title{position:absolute;left:40px;top:120px;width:430px;font-family:"Oswald",Arial,sans-serif;font-size:17px;line-height:22px;color:var(--white);text-transform:uppercase}
.hero-text{position:absolute;left:40px;top:170px;width:330px;font-size:8px;line-height:12px;color:var(--white)}
.btn{display:inline-block;background:var(--nav);color:var(--white);font-size:8px;font-weight:700;border-radius:12px;padding:6px 16px;text-transform:uppercase}
.hero .btn{position:absolute;left:40px;top:200px}
.dots{position:absolute;left:44px;top:300px;display:flex;gap:5px}
.dots span{width:7px;height:7px;border-radius:50%;background:var(--blue-soft)}
.dots span.on{background:var(--blue)}
.welcome{position:absolute;left:0;top:420px;width:867px;text-align:center}
.section-title{font-family:"Oswald",Arial,sans-serif;font-weight:400;font-size:17px;color:var(--blue);text-transform:uppercase;letter-spacing:.5px}
.welcome p{width:570px;margin:10px auto 14px;font-size:8px;line-height:12px;color:var(--muted)}
.services-head{position:absolute;left:0;top:543px;width:867px;display:flex;justify-content:center;align-items:center;gap:12px}
.services-head i{display:block;width:60px;height:1px;background:var(--blue-soft)}
.card{position:absolute;top:592px;width:195px}
.card .photo{height:130px;background:linear-gradient(160deg,#e8d3c6,#c98d79)}
.card h3{margin:8px 0 4px;font-size:8.5px;font-weight:700;color:var(--blue);text-transform:uppercase}
.card p{font-size:7.5px;line-height:11px;color:var(--muted)}
.booking{position:absolute;left:100px;top:823px;width:667px;height:150px;background:linear-gradient(90deg,#eef3f8,#dfe8f1 60%,#c9d6e4);text-align:center;padding-top:16px}
.form-grid{position:absolute;left:40px;top:58px;width:587px;display:grid;grid-template-columns:repeat(3,1fr);gap:10px 14px}
.field{height:24px;background:var(--white);border:1px solid #cfd8e2;font-size:8px;color:#999;text-align:left;padding:7px 10px}
.field.submit{background:var(--nav);color:var(--white);font-weight:700;text-align:center;border:none}
.site-footer{position:absolute;left:0;top:985px;width:867px;height:185px;background:var(--footer);color:#ccc}
.footer-col{position:absolute;top:18px}
.footer-col h4{font-family:"Oswald",Arial,sans-serif;font-weight:400;font-size:13px;color:var(--white);margin-bottom:8px}
.footer-col li{list-style:none;font-size:8px;line-height:14px}
.map{position:absolute;left:488px;top:22px;width:110px;height:80px;background:linear-gradient(135deg,#e4e1d6,#c9d3c3)}
.social{display:flex;gap:5px}
.social span{width:16px;height:16px;background:var(--nav)}
.social span:nth-child(4){background:#fff}
.footer-bar{position:absolute;left:0;top:1170px;width:867px;height:30px;background:var(--footer-bar);color:#aaa;font-size:7.5px;text-align:center;line-height:30px}
</style>
</head>
<body>
<header class="site-header">
  <div class="brand">CALVEXA LASER PAIN RELIEF</div>
  <div class="phone-pill"><span class="ico"><svg width="10" height="10" viewBox="0 0 24 24"><path fill="#3e8fd1" d="M6.6 10.8a15.1 15.1 0 0 0 6.6 6.6l2.2-2.2c.3-.3.7-.4 1-.2 1.1.4 2.3.6 3.6.6.6 0 1 .4 1 1V20c0 .6-.4 1-1 1A17 17 0 0 1 3 4c0-.6.4-1 1-1h3.5c.6 0 1 .4 1 1 0 1.3.2 2.5.6 3.6.1.3 0 .7-.2 1z"/></svg></span>(555) 014-2280</div>
</header>
<section class="hero">
  <div class="hero-photo" role="img" aria-label="Close-up photo of a patient's eye with a glowing laser treatment ring"></div>
  <div class="hero-band"></div>
  <h1 class="hero-title">Nam libero tempore, cum soluta nobis est eligendi optio cumque</h1>
  <p class="hero-text">Lorem ipsum dolor sit amet, consectetur adipiscing elit, sed do eiusmod tempor incididunt ut labore et dolore magna aliqua.</p>
  <span class="btn">Learn more</span>
  <div class="dots"><span class="on"></span><span></span><span></span><span></span></div>
</section>
<nav class="main-nav">
  <a>HOME</a><a>WHY CHOOSE US</a><a>TREATABLE CONDITIONS</a><a>TESTIMONIALS</a><a>FAQ</a><a>FRANCHISING</a><a class="active">CONTACT US</a>
</nav>
<section class="welcome">
  <h2 class="section-title">Welcome to our website</h2>
  <p>Temporibus autem quibusdam et aut officiis debitis aut rerum necessitatibus saepe eveniet ut et voluptates repudiandae sint et molestiae non recusandae. Itaque earum rerum hic tenetur a sapiente delectus, ut aut reiciendis voluptatibus maiores alias consequatur aut perferendis doloribus asperiores repellat.</p>
  <span class="btn">Read more</span>
</section>
<div class="services-head"><i></i><h2 class="section-title">Services</h2><i></i></div>
<article class="card" style="left:110px">
  <div class="photo" role="img" aria-label="Photo of a person holding their lower back in pain"></div>
  <h3>Relieve back pain</h3>
  <p>Neque porro quisquam est, qui dolorem ipsum quia dolor sit amet, consectetur, adipisci velit, sed quia.</p>
</article>
<article class="card" style="left:334px">
  <div class="photo" role="img" aria-label="Photo of a person holding a painful knee"></div>
  <h3>Relieve knee pain</h3>
  <p>Neque porro quisquam est, qui dolorem ipsum quia dolor sit amet, consectetur, adipisci velit, sed quia.</p>
</article>
<article class="card" style="left:558px">
  <div class="photo" role="img" aria-label="Photo of a person holding a sore shoulder"></div>
  <h3>Relieve shoulder pain</h3>
  <p>Neque porro quisquam est, qui dolorem ipsum quia dolor sit amet, consectetur, adipisci velit, sed quia.</p>
</article>
<section class="booking" role="img" aria-label="Soft background photo of a clinic treatment room">
  <h2 class="section-title">Book and appointment</h2>
  <div class="form-grid">
    <div class="field">First Name</div><div class="field">Last Name</div><div class="field">Email</div>
    <div class="field">Phone Number</div><div class="field">Message</div><div class="field submit">BOOK AN APPOINTMENT</div>
  </div>
</section>
<footer class="site-footer">
  <div class="footer-col" style="left:38px"><h4>Quick Links</h4><ul><li>Home</li><li>Why Choose Us</li><li>Treatable Conditions</li><li>Testimonials</li><li>FAQ</li><li>Franchising</li></ul></div>
  <div class="footer-col" style="left:210px"><h4>My Account</h4><ul><li>Login</li><li>Sign Up</li><li>Privacy</li><li>Terms &amp; Conditions</li></ul></div>
  <div class="footer-col" style="left:360px"><h4>Contact Us</h4><ul><li>28 Harbor Street, Suite 4</li><li>Lakeview</li><li>(555) 014-2280</li><li>info@calvexa.com</li></ul></div>
  <div class="map" role="img" aria-label="Street map showing the clinic location"></div>
  <div class="footer-col" style="left:690px"><h4>Follow Us</h4><div class="social"><span></span><span></span><span></span><span></span></div></div>
</footer>
<div class="footer-bar">© 2024 calvexalaserpainrelief.com | All Rights Reserved</div>
</body>
</html>
```